Letterhead and Corporate Stationary Design Project

I would like the following designed:
1. Corporate Letterhead
2. Compliment Slips
3. Business Cards(2)

I have attached word document that outlines the text to be contained for all 3. The logo is fine as is and can be used in the design.
I only need letterhead to be designed for contest, the successful applicant can desisgn other 2 items after being awarded the job

Target Market(s)

Information Technology

Industry/Entity Type

Business

Requirements
Must have
• Border around entire letter that matches colours in logo
Clearly identifiable letterhead and footer
Nice to have
• Watermark

```html
<!DOCTYPE html>
<html lang="en">
<head>
<meta charset="utf-8">
<title>Corvane Business Solutions – Letterhead</title>
<link rel="stylesheet" href="https://fonts.googleapis.com/css2?family=Arimo:wght@400;700&family=Caveat:wght@500&display=swap">
<style>
  :root {
    --backdrop: #a4ab93;
    --paper: #ffffff;
    --ink: #1f1f1f;
    --ink-soft: #3a3a3a;
    --brand-sky: #3fa9f5;
    --brand-navy: #1a2fb8;
    --rule: #5a74e6;
    --watermark: #eceeee;
  }
  * { box-sizing: border-box; margin: 0; padding: 0; }
  html, body {
    width: 1200px; height: 900px; overflow: hidden;
    background: var(--backdrop);
  }
  .letterhead {
    position: absolute; left: 330px; top: 62px;
    width: 545px; height: 770px;
    background: var(--paper);
    font-family: "Arimo", Arial, sans-serif;
    color: var(--ink);
  }
  .brand {
    position: absolute; left: 28px; top: 34px;
    display: flex; align-items: center; gap: 8px;
  }
  .brand-dot {
    width: 26px; height: 26px; border-radius: 50%;
    background: var(--brand-sky);
  }
  .brand-name {
    font-size: 30px; font-weight: 400; color: var(--brand-sky);
    letter-spacing: 0.5px; line-height: 1;
  }
  .sender-address {
    position: absolute; right: 26px; top: 32px;
    text-align: right; font-style: normal;
    font-size: 8px; line-height: 10px; color: var(--ink-soft);
  }
  .rule {
    position: absolute; left: 26px; right: 26px; height: 1px;
    background: var(--rule);
  }
  .rule--header { top: 89px; }
  .rule--footer { top: 726px; }
  .letter-body {
    position: absolute; left: 26px; top: 115px; width: 493px;
    font-size: 8.3px; line-height: 10.4px; color: var(--ink-soft);
  }
  .salutation { font-weight: 700; color: var(--ink); margin-bottom: 8px; }
  .letter-body p.copy {
    text-align: justify; hyphens: auto; margin-bottom: 10.4px;
  }
  .sign-off { margin-top: 16px; }
  .signature {
    font-family: "Caveat", cursive; font-size: 19px; line-height: 16px;
    color: var(--ink);
  }
  .signatory-role { font-weight: 700; color: var(--ink); }
  .watermark {
    position: absolute; left: 288px; top: 500px;
    width: 225px; height: 180px;
  }
  .company-footer {
    position: absolute; left: 0; right: 0; top: 735px;
    text-align: center; font-size: 7.6px; color: var(--ink-soft);
  }
  .company-footer .sep { color: var(--brand-navy); }
</style>
</head>
<body>
  <main class="letterhead">
    <header>
      <div class="brand">
        <span class="brand-dot"></span>
        <span class="brand-name">corvane</span>
      </div>
      <address class="sender-address">
        Corvane Business Solutions<br>
        Mill House, 8 Bridge Street, Kilcarran<br>
        Co. Laois, Ireland<br>
        tel: + 353 44 9015530<br>
        www.corvane.ie
      </address>
      <div class="rule rule--header"></div>
    </header>

    <svg class="watermark" role="img" aria-label="Faint brand watermark" viewBox="0 0 225 180">
      <circle cx="112" cy="90" r="80" fill="var(--watermark)"/>
    </svg>

    <section class="letter-body">
      <p class="salutation">Lorem ipsum,</p>
      <p class="copy">Lorem ipsum dolor sit amet, consectetur adipiscing elit. In sit amet ipsum purus. Sed imperdiet vulputate nisi, in aliquam mauris varius et. Morbi a nisi ac ligula gravida auctor sed sed elit. Nam ac nunc sit amet neque scelerisque tristique vel ut ligula. Mauris nec ipsum sapien, vel tincidunt sapien. Pellentesque sit amet lorem eros, rutrum sagittis ligula. Phasellus at neque id felis adipiscing pulvinar nec id mauris. In hac habitasse platea dictumst. Nam fermentum iaculis malesuada. Mauris vitae odio at sem ornare tempor in vel odio. Ut venenatis pellentesque. Sed tincidunt leo id elit scelerisque vestibulum.</p>
      <p class="copy">Vestibulum ultrices nunc sed urna tincidunt ut faucibus elit molestie. Integer ultrices mauris at lacus ultrices egestas. Phasellus in dui nulla. Cras justo est, volutpat in semper sit amet, viverra vel purus. Vestibulum eget odio odio. Pellentesque gravida arcu eu lectus accumsan et lobortis tortor fringilla. Curabitur ultricies tempus elit, ut congue diam porta sed. Quisque nec felis quam, at mollis nisl. Curabitur rutrum libero eu justo congue pulvinar nec eu magna. Nunc vel augue in nunc lacinia tincidunt nec sit amet ligula. Vivamus consequat sollicitudin semper.</p>
      <p class="copy">Vivamus lobortis tincidunt tellus quis sodales. Nullam sodales lacinia libero. Vivamus rhoncus quam a urna porta tempus. Proin arcu metus, cursus vel ornare eu, posuere id augue. Suspendisse auctor posuere mauris, rutrum luctus augue vehicula a. Maecenas id tristique est. Sed a felis dolor, et placerat lacus. Cras commodo nunc eu velit iaculis ut porta tortor laoreet. Integer bibendum nunc at sapien consectetur vel scelerisque dolor suscipit. Nam sagittis risus id ante auctor ut fermentum sapien lacinia.</p>
      <p class="copy">Sed viverra condimentum dolor, et condimentum justo accumsan in. Aliquam erat volutpat. Nullam quis justo elit. Nullam nec turpis augue, in ultrices purus. Suspendisse nulla dolor, mollis commodo faucibus at, malesuada in arcu. Nam quis vehicula justo. Donec pretium egestas justo a dictum. Nam sit amet euismod elit. Curabitur a mi id ipsum vehicula pharetra at quis urna. Etiam suscipit, quam ut rutrum lacinia, dui tellus luctus enim, vel consequat magna mi rutrum sapien. Ut urna velit, accumsan sed consequat eget, malesuada non odio.</p>
      <p class="copy">Suspendisse vitae viverra risus. Integer ultricies tristique risus id dapibus. Donec non dolor lacus, eget cursus quam. Sed pharetra posuere consectetur. Proin sit amet diam nisl, eu sodales leo. Ut est mauris, aliquam id gravida at, sagittis at tortor. Quisque commodo euismod nisl id convallis. Aenean sed felis nec ligula elementum pellentesque sed in enim. Integer ac rhoncus velit.</p>
      <div class="sign-off">
        <p class="signature">Your name</p>
        <p class="signatory-role">Manager</p>
      </div>
    </section>

    <footer>
      <div class="rule rule--footer"></div>
      <p class="company-footer">Corvane Business Solutions Limited <span class="sep">•</span> Company Registration 512839 <span class="sep">•</span> VAT No IE5128390K</p>
    </footer>
  </main>
</body>
</html>
```